Pain Seminar Flyer 8.5x11

We are having a FREE seminar on Pain for our Bootcamp members at our gym. We are looking for a great looking flyer with pictures and a design to draw people in. I have attached our logo, pictures of the 2 speakers and a Word document of the flyer information needed. PLEASE PLEASE make our head shots small and in a circle like the example flyer we attached but obviously make the flyer much much nicer than the example. Also we attached pic ideas about pain.
- This must be in PSD. format WITH LAYERS and fonts so we can edit the time or reuse the flyer.
- Size 8.5x11
- Attached info. with pics and logo (along with other pics of pain!)
Thank you!
Gym

```html
<!DOCTYPE html>
<html lang="en">
<head>
<meta charset="utf-8">
<title>Pain Seminar Flyer</title>
<link href="https://fonts.googleapis.com/css2?family=Roboto+Condensed:wght@700;800&family=Lato:wght@400;700;900&display=swap" rel="stylesheet">
<style>
  :root {
    --page-bg: #ececec;
    --blue: #0d64a8;
    --blue-dark: #0a4f8c;
    --blue-light: #5aa6dc;
    --orange: #f5900f;
    --orange-light: #fbb040;
    --orange-text: #f7a600;
    --ink: #1d1d1d;
    --grey-text: #555;
    --white: #ffffff;
    --photo-tone: #8a8f7a;
    --photo-tone-2: #c9b7a4;
  }
  * { margin: 0; padding: 0; box-sizing: border-box; }
  html, body { width: 1200px; height: 900px; overflow: hidden; }
  body { background: var(--page-bg); position: relative; font-family: "Lato", sans-serif; }

  .flyer {
    position: absolute; left: 304px; top: 132px; width: 592px; height: 768px;
    background: linear-gradient(#f4f4f4, #ffffff 40%, #f3f3f3);
    overflow: hidden;
  }
  .flyer-shapes { position: absolute; inset: 0; }

  .headline { position: absolute; left: 0; top: 16px; width: 592px; height: 100px; }
  .headline-parts {
    position: absolute; right: 360px; top: 4px; text-align: right;
    font-family: "Roboto Condensed", sans-serif; font-weight: 800;
    color: var(--white); font-size: 31px; line-height: 29px;
    text-shadow: 1px 2px 2px rgba(0,0,0,.35);
  }
  .headline-pain {
    position: absolute; left: 236px; top: -14px;
    font-family: "Roboto Condensed", sans-serif; font-weight: 800;
    font-size: 116px; line-height: 1; color: var(--white);
    text-shadow: 2px 3px 3px rgba(0,0,0,.35);
  }

  .title { position: absolute; left: 0; width: 592px; text-align: center;
    font-family: "Roboto Condensed", sans-serif; font-weight: 800; }
  .title-free { top: 166px; font-size: 74px; line-height: 1; color: var(--orange-text);
    text-shadow: 2px 3px 2px rgba(0,0,0,.25); }
  .title-sub { top: 236px; font-size: 53px; line-height: 1; color: var(--blue-dark);
    text-shadow: 2px 2px 2px rgba(0,0,0,.2); }
  .reservations { position: absolute; top: 301px; left: 0; width: 592px; text-align: center;
    font-size: 13.5px; letter-spacing: .6px; color: var(--grey-text); }

  .topics { position: absolute; left: 48px; top: 344px; list-style: none; }
  .topics li { display: flex; align-items: center; height: 38px;
    font-weight: 700; font-size: 18.5px; color: var(--ink); }
  .topics svg { width: 20px; height: 20px; margin-right: 11px; }

  .date-box { position: absolute; left: 446px; top: 346px; width: 148px; height: 89px;
    background: linear-gradient(var(--orange-light), var(--orange));
    color: var(--white); text-align: center;
    font-family: "Roboto Condensed", sans-serif; font-weight: 800;
    box-shadow: 1px 2px 3px rgba(0,0,0,.3); padding-top: 7px; }
  .date-day { font-size: 20px; line-height: 23px; }
  .date-date { font-size: 27px; line-height: 29px; }
  .date-time { font-size: 20px; line-height: 22px; }
  .phone-box { position: absolute; left: 448px; top: 443px; width: 141px; height: 33px;
    background: var(--blue); color: var(--white); text-align: center;
    font-family: "Roboto Condensed", sans-serif; font-weight: 800; font-size: 22px; line-height: 33px;
    transform: rotate(-2deg); box-shadow: 1px 2px 3px rgba(0,0,0,.3); }

  .speaker-photo { position: absolute; border-radius: 50%; border: 5px solid var(--white);
    box-shadow: 0 2px 5px rgba(0,0,0,.3); }
  .speaker-photo--left { left: 30px; top: 514px; width: 144px; height: 144px;
    background: radial-gradient(circle at 50% 40%, var(--photo-tone-2), var(--photo-tone)); }
  .speaker-photo--right { left: 426px; top: 492px; width: 148px; height: 148px;
    background: radial-gradient(circle at 50% 40%, #c98a6a, #bdbdbd); }
  .speaker-name { position: absolute; font-weight: 900; font-size: 14.5px; color: var(--blue); line-height: 18px; }
  .speaker-cred { display: block; font-weight: 400; font-size: 12px; color: var(--blue-dark); }
  .speaker-name--left { left: 186px; top: 571px; }
  .speaker-name--right { right: 179px; top: 557px; text-align: right; }

  .brand { position: absolute; left: 25px; top: 678px; width: 225px; height: 72px;
    background: var(--white); display: flex; align-items: center; justify-content: center; gap: 8px;
    font-family: "Lato", sans-serif; font-weight: 900; font-size: 20px; color: var(--blue); }
  .brand-mark { width: 14px; height: 14px; background: var(--orange); border-radius: 50%; }
  .venue { position: absolute; left: 271px; top: 678px; color: var(--white);
    font-size: 14.5px; line-height: 19px; letter-spacing: .3px; }
</style>
</head>
<body>
  <main class="flyer">
    <svg class="flyer-shapes" viewBox="0 0 592 768" width="592" height="768" aria-hidden="true">
      <path d="M0 0H592V132C420 118 200 122 0 166Z" fill="#5aa6dc"/>
      <path d="M0 0H592V118C420 108 200 110 0 140Z" fill="#0d64a8"/>
      <path d="M0 628C200 648 430 620 592 530V768H0Z" fill="#fbb040"/>
      <path d="M0 640C210 664 440 640 592 556V768H0Z" fill="#f5900f"/>
    </svg>

    <header class="headline">
      <div class="headline-parts">BACK<br>SHOULDER<br>KNEE</div>
      <div class="headline-pain">PAIN?</div>
    </header>

    <h1 class="title title-free">FREE SEMINAR</h1>
    <h2 class="title title-sub">ON HOW TO STOP PAIN</h2>
    <p class="reservations">RESERVATIONS REQUIRED.&nbsp; LIMITED SPACE SO DON’T WAIT TO SIGN UP</p>

    <ul class="topics">
      <li><svg viewBox="0 0 20 20"><circle cx="10" cy="10" r="8.5" fill="none" stroke="#f5900f" stroke-width="2"/><path d="M8 6l4 4-4 4" fill="none" stroke="#f5900f" stroke-width="2.4"/></svg>How to Get Out of Pain</li>
      <li><svg viewBox="0 0 20 20"><circle cx="10" cy="10" r="8.5" fill="none" stroke="#f5900f" stroke-width="2"/><path d="M8 6l4 4-4 4" fill="none" stroke="#f5900f" stroke-width="2.4"/></svg>What to do When an Exercise Hurts</li>
      <li><svg viewBox="0 0 20 20"><circle cx="10" cy="10" r="8.5" fill="none" stroke="#f5900f" stroke-width="2"/><path d="M8 6l4 4-4 4" fill="none" stroke="#f5900f" stroke-width="2.4"/></svg>How Exercise Helps Pain</li>
      <li><svg viewBox="0 0 20 20"><circle cx="10" cy="10" r="8.5" fill="none" stroke="#f5900f" stroke-width="2"/><path d="M8 6l4 4-4 4" fill="none" stroke="#f5900f" stroke-width="2.4"/></svg>Q &amp; A to Fine Extraordinary Health</li>
    </ul>

    <div class="date-box">
      <div class="date-day">THURSDAY</div>
      <div class="date-date">APRIL 13th</div>
      <div class="date-time">7:30PM-9PM</div>
    </div>
    <div class="phone-box">303-555-0148</div>

    <div class="speaker-photo speaker-photo--left" role="img" aria-label="Head shot of speaker Daniel Hart"></div>
    <p class="speaker-name speaker-name--left">Daniel Hart<span class="speaker-cred">PT, DPT, OCS</span></p>
    <p class="speaker-name speaker-name--right">Marcus Reed<span class="speaker-cred">MS, CSCS, FMS</span></p>
    <div class="speaker-photo speaker-photo--right" role="img" aria-label="Head shot of speaker Marcus Reed"></div>

    <div class="brand"><span class="brand-mark"></span>MoveWell Bootcamps</div>
    <address class="venue" style="font-style:normal">MOVEWELL PERSONAL TRAINING STUDIO<br>18 W. Elm St. Lakeview, CO 80000</address>
  </main>
</body>
</html>
```